Professional PowerPoint Template for Data Reports, Presentations

We are a small leadership coaching/consulting firm and would like to update our PowerPoint template that we use with our clients, who are typically mid-senior level company professionals. I've attached a sample Powerpoint as well as our branding guide. The cover page is what needs the most work - just doesn't look current/professional enough. We do want to keep the pages after that clean, with come color but enough space for text and graphics.
Target Market(s)
Senior mgmt and HR executives in small-mid sized companies
Font styles to use
Sans Serif
Requirements
Must have
- Professional
- Clean
- Tied to company color scheme/logo
Nice to have
- Our title pages don't usually have many words on them; we'd like a design that has a lot of color - probably still using mainly our blue but accented with other colors.
- Need simple but smart looking pages after cover with lot of space; mostly we have text on the slides. Currently this is often in bullet point style, but we could probably upgrade the options there.
Should not have
- Anything that looks like a marketing style, as we typically use these with our current clients to share results of data collected, project plans, etc.

```html
<!DOCTYPE html>
<html lang="en">
<head>
<meta charset="utf-8">
<title>Keelway Presentation Template</title>
<link rel="stylesheet" href="https://fonts.googleapis.com/css2?family=Arimo:wght@400;700&family=Montserrat:wght@400;500&display=swap">
<style>
:root{
  --blue:#245d8c;
  --blue-deep:#1b4e78;
  --navy:#123a58;
  --teal:#6cb4a6;
  --orange:#e0592c;
  --grey:#c7ccd0;
  --lilac:#a897c8;
  --ink:#555c63;
  --paper:#ffffff;
  --page:#ffffff;
}
*{box-sizing:border-box;margin:0;padding:0}
html,body{width:686px;height:1200px;overflow:hidden;background:var(--page)}
body{position:relative;font-family:"Arimo",Arial,sans-serif;color:var(--ink)}
.slide{position:absolute;width:337px;height:191px;overflow:hidden;background:var(--paper);box-shadow:0 1px 4px rgba(0,0,0,.18)}
.col-l{left:3px}.col-r{left:346px}
.row1{top:5px}.row2{top:204px}.row3{top:405px}.row4{top:605px}.row5{top:804px}.row6{top:1005px}

.photo{position:absolute}
.brand{position:absolute;display:flex;align-items:center;gap:5px;font-family:"Montserrat",sans-serif;font-weight:400;letter-spacing:2.5px;color:#fff}
.brand .dot{border:2px solid currentColor;border-radius:50%}
.brand-lg{font-size:15px}.brand-lg .dot{width:17px;height:17px}
.brand-sm{font-size:4.6px;letter-spacing:.8px;flex-direction:column;gap:2px}
.brand-sm .dot{width:9px;height:9px;border-width:1.3px}

.side-band{position:absolute;right:0;top:0;width:31px;height:100%;background:var(--blue)}
.side-band .brand-sm{left:0;width:31px;top:6px}
.page-no{position:absolute;right:12px;bottom:5px;font-size:3.5px;color:#fff}
.footer{position:absolute;left:7px;bottom:5px;font-size:3.2px;color:#8a9096}
.slide-title{position:absolute;left:8px;top:11px;font-size:14px;font-weight:700;color:var(--blue)}
.body-copy{font-size:4.1px;line-height:1.32;text-align:justify;color:#6a7076}

.cover-ring{position:absolute;border-radius:50%;border:22px solid rgba(255,255,255,.35)}
.cover-title{position:absolute;right:22px;top:115px;font-size:14px;font-weight:700}
.date-pill{position:absolute;right:22px;top:146px;width:44px;height:14px;border-radius:7px;background:var(--teal);color:#fff;font-size:5.5px;text-align:center;line-height:14px}
.confidential{position:absolute;right:22px;bottom:17px;font-size:5.2px;letter-spacing:.2px}

.agenda-grid{position:absolute;left:28px;top:44px;display:grid;grid-template-columns:repeat(4,66px);row-gap:14px}
.agenda-item{display:flex;flex-direction:column;align-items:center;gap:3px;color:var(--blue);font-weight:700;font-size:6.8px}
.agenda-item .num{width:32px;height:32px;border-radius:50%;border:3.5px solid var(--blue);display:flex;align-items:center;justify-content:center;font-size:8px}

.para-block{position:absolute;left:12px;top:48px;width:285px;display:flex;flex-direction:column;gap:6px}
.bullet-list{position:absolute;left:10px;top:50px;width:287px;list-style:none;display:flex;flex-direction:column;gap:6px}
.bullet-list li,.mini-list li{position:relative;padding-left:9px}
.bullet-list li::before,.mini-list li::before{content:"";position:absolute;left:0;top:1px;width:3px;height:3px;background:var(--blue)}
.mini-list{list-style:none;display:flex;flex-direction:column;gap:2px}

.mo-left{position:absolute;left:0;top:40px;width:70px;height:142px;background:var(--navy);color:#fff;padding:8px 6px}
.mo-item{margin-bottom:14px}
.mo-icon{width:8px;height:8px;border:1px solid #fff;border-radius:2px;margin-bottom:5px}
.mo-head{font-size:5px;margin-bottom:2px}
.mo-text{font-size:3.6px;font-weight:700;line-height:1.3}
.mo-right{position:absolute;left:240px;top:40px;width:66px;height:64px;background:var(--blue-deep);color:#fff;padding:6px 5px}
.mo-card{position:absolute;left:72px;top:103px;width:234px;padding:6px 8px}
.mo-card h3{font-size:5.4px;color:var(--blue);margin-bottom:4px;font-weight:700}
.mo-card p{font-size:3.7px;line-height:1.8;color:#7a8086}

.team-name{font-size:6.5px;color:var(--orange)}
.team-role{font-size:3.8px;color:#8a9096}
.team-deg{font-size:4.5px;color:var(--blue);font-weight:700;margin:1px 0 2px}
.avatar{border-radius:50%;background:radial-gradient(circle at 50% 40%,#d9d4cf,#8f8a86)}
.team-entry{position:absolute;display:flex;gap:6px}
.team-entry .avatar{width:28px;height:28px;flex:none;margin-top:4px}
.team-entry .body-copy{text-align:left;width:80px}

.thanks{position:absolute;left:178px;top:78px;font-size:13.5px;font-weight:700;color:#fff}
.contact{position:absolute;left:182px;top:104px;list-style:none;display:flex;flex-direction:column;gap:4.5px;color:#fff;font-size:3.8px}
.contact li{display:flex;align-items:center;gap:5px}
.contact svg{width:6px;height:6px;flex:none}
</style>
</head>
<body>

<!-- Cover, dark -->
<section class="slide col-l row1" style="background:var(--blue)">
  <div class="photo" role="img" aria-label="Sailboats on open water under a cloudy sky, blue tinted" style="inset:0;background:linear-gradient(180deg,#4f7ea6 0%,#2e6591 55%,#1f557f 100%)"></div>
  <div class="cover-ring" style="left:-70px;top:-10px;width:200px;height:200px"></div>
  <div class="brand brand-lg" style="left:211px;top:38px"><span class="dot"></span>KEELWAY</div>
  <h1 class="cover-title" style="color:#fff">Your Title</h1>
  <div class="date-pill">Date</div>
  <p class="confidential" style="color:#fff">CONFIDENTIAL</p>
</section>

<!-- Cover, light -->
<section class="slide col-r row1">
  <div class="photo" role="img" aria-label="Pale washed-out sailboats on the sea" style="inset:0;background:linear-gradient(180deg,#e9eef3 0%,#d7e0e8 60%,#eef2f5 100%)"></div>
  <div class="cover-ring" style="left:-30px;top:-10px;width:200px;height:200px;border-color:rgba(36,93,140,.75)"></div>
  <div class="brand brand-lg" style="left:211px;top:38px;color:var(--blue)"><span class="dot"></span>KEELWAY</div>
  <h1 class="cover-title" style="color:var(--blue)">Your Title</h1>
  <div class="date-pill">Date</div>
  <p class="confidential" style="color:var(--blue)">CONFIDENTIAL</p>
</section>

<!-- Agenda -->
<section class="slide col-l row2">
  <div class="photo" role="img" aria-label="Faint office desk scene in light grey" style="inset:0;background:linear-gradient(120deg,#fbfbfb 0%,#eeeeee 60%,#f7f7f7 100%)"></div>
  <h2 class="slide-title">Agenda</h2>
  <div class="agenda-grid">
    <div class="agenda-item"><span class="num">1</span>Agenda 1</div>
    <div class="agenda-item"><span class="num">2</span>Agenda 2</div>
    <div class="agenda-item"><span class="num">3</span>Agenda 3</div>
    <div class="agenda-item"><span class="num">4</span>Agenda 4</div>
    <div class="agenda-item"><span class="num">5</span>Agenda 5</div>
    <div class="agenda-item"><span class="num">6</span>Agenda 6</div>
    <div class="agenda-item"><span class="num">7</span>Agenda 7</div>
    <div class="agenda-item"><span class="num">8</span>Agenda 8</div>
  </div>
</section>

<!-- Text slide -->
<section class="slide col-r row2">
  <h2 class="slide-title">Text Slide</h2>
  <div class="side-band"><div class="brand brand-sm"><span class="dot"></span>KEELWAY</div><span class="page-no">4</span></div>
  <div class="para-block">
    <p class="body-copy">Lorem ipsum dolor sit amet, consectetur adipiscing elit, sed do eiusmod tempor incididunt ut labore et dolore magna aliqua. Ut enim ad minim veniam, quis nostrud exercitation ullamco laboris nisi ut aliquip ex ea commodo consequat. Duis aute irure dolor in reprehenderit in voluptate velit esse cillum dolore eu fugiat nulla pariatur. Excepteur sint occaecat cupidatat non proident, sunt in culpa qui officia deserunt mollit anim id est laborum. Sed ut perspiciatis unde omnis iste natus error sit voluptatem accusantium doloremque laudantium, totam rem aperiam.</p>
    <p class="body-copy">Lorem ipsum dolor sit amet, consectetur adipiscing elit, sed do eiusmod tempor incididunt ut labore et dolore magna aliqua. Ut enim ad minim veniam, quis nostrud exercitation ullamco laboris nisi ut aliquip ex ea commodo consequat. Duis aute irure dolor in reprehenderit in voluptate velit esse cillum dolore eu fugiat nulla pariatur. Excepteur sint occaecat cupidatat non proident, sunt in culpa qui officia deserunt mollit anim id est laborum. Sed ut perspiciatis unde omnis iste natus error sit voluptatem accusantium doloremque laudantium, totam rem aperiam.</p>
    <p class="body-copy">Lorem ipsum dolor sit amet, consectetur adipiscing elit, sed do eiusmod tempor incididunt ut labore et dolore magna aliqua. Ut enim ad minim veniam, quis nostrud exercitation ullamco laboris nisi ut aliquip ex ea commodo consequat. Duis aute irure dolor in reprehenderit in voluptate velit esse cillum dolore eu fugiat nulla pariatur. Excepteur sint occaecat cupidatat non proident, sunt in culpa qui officia deserunt mollit anim id est laborum. Sed ut perspiciatis unde omnis iste natus error sit voluptatem accusantium doloremque laudantium, totam rem aperiam.</p>
  </div>
  <p class="footer">© Keelway Company · www.keelwayco.com/000-000-0000</p>
</section>

<!-- Divider -->
<section class="slide col-l row3" style="background:var(--teal)">
  <div class="photo" role="img" aria-label="Soft teal-tinted chess pieces on a board" style="inset:0;background:linear-gradient(180deg,#7dbdb0 0%,#6cb4a6 55%,#64ab9d 100%)"></div>
  <div class="cover-ring" style="left:-60px;top:-20px;width:210px;height:210px;border-color:rgba(18,58,88,.8)"></div>
  <div class="brand brand-lg" style="left:211px;top:34px"><span class="dot"></span>KEELWAY</div>
  <h1 class="cover-title" style="color:#fff;top:110px">Dividr Page</h1>
  <p class="confidential" style="color:#fff">CONFIDENTIAL</p>
</section>

<!-- Bullets slide -->
<section class="slide col-r row3">
  <h2 class="slide-title">Bullets Slide</h2>
  <div class="side-band"><div class="brand brand-sm"><span class="dot"></span>KEELWAY</div><span class="page-no">5</span></div>
  <ul class="bullet-list body-copy">
    <li>Lorem ipsum dolor sit amet, consectetur adipiscing elit, sed do eiusmod tempor incididunt ut labore et dolore magna aliqua. Ut enim ad minim veniam, quis nostrud exercitation ullamco laboris nisi ut aliquip ex ea commodo consequat. Duis aute irure dolor in reprehenderit in voluptate velit esse cillum dolore eu fugiat nulla pariatur. Excepteur sint occaecat cupidatat non proident, sunt in culpa qui officia deserunt mollit anim id est laborum. Sed ut perspiciatis unde omnis iste natus error sit voluptatem accusantium doloremque laudantium, totam rem aperiam.</li>
    <li>Lorem ipsum dolor sit amet, consectetur adipiscing elit, sed do eiusmod tempor incididunt ut labore et dolore magna aliqua. Ut enim ad minim veniam, quis nostrud exercitation ullamco laboris nisi ut aliquip ex ea commodo consequat. Duis aute irure dolor in reprehenderit in voluptate velit esse cillum dolore eu fugiat nulla pariatur. Excepteur sint occaecat cupidatat non proident, sunt in culpa qui officia deserunt mollit anim id est laborum. Sed ut perspiciatis unde omnis iste natus error sit voluptatem accusantium doloremque laudantium, totam rem aperiam.</li>
    <li>Lorem ipsum dolor sit amet, consectetur adipiscing elit, sed do eiusmod tempor incididunt ut labore et dolore magna aliqua. Ut enim ad minim veniam, quis nostrud exercitation ullamco laboris nisi ut aliquip ex ea commodo consequat. Duis aute irure dolor in reprehenderit in voluptate velit esse cillum dolore eu fugiat nulla pariatur. Excepteur sint occaecat cupidatat non proident, sunt in culpa qui officia deserunt mollit anim id est laborum. Sed ut perspiciatis unde omnis iste natus error sit voluptatem accusantium doloremque laudantium, totam rem aperiam.</li>
  </ul>
  <p class="footer">© Keelway Company · www.keelwayco.com/000-000-0000</p>
</section>

<!-- Market overview -->
<section class="slide col-l row4">
  <h2 class="slide-title">Market Overview</h2>
  <div class="side-band"><div class="brand brand-sm"><span class="dot"></span>KEELWAY</div><span class="page-no">7</span></div>
  <div class="mo-left">
    <div class="mo-item"><div class="mo-icon"></div><p class="mo-head">Heading Text</p><p class="mo-text">dolore aliqua. Lorem ipsum dolor sit amet, consectetur adipiscing elit, sed do eiusmod tempor incididunt ut</p></div>
    <div class="mo-item"><div class="mo-icon"></div><p class="mo-head">Heading Text</p><p class="mo-text">dolore aliqua. Lorem ipsum dolor sit amet, consectetur adipiscing elit, sed do eiusmod tempor incididunt ut</p></div>
  </div>
  <div class="photo" role="img" aria-label="Glass chess pieces on a dark board" style="left:72px;top:40px;width:93px;height:63px;background:linear-gradient(180deg,#2b2a28 0%,#6d655a 60%,#3a3834 100%)"></div>
  <svg style="position:absolute;left:165px;top:40px" width="75" height="63" viewBox="0 0 75 63">
    <circle cx="37.5" cy="31.5" r="22" fill="none" stroke="#e4e9ee" stroke-width="5"/>
    <circle cx="37.5" cy="31.5" r="22" fill="none" stroke="#3f8ccc" stroke-width="5" stroke-dasharray="82.9 138.2" transform="rotate(-90 37.5 31.5)"/>
    <text x="37.5" y="35.5" text-anchor="middle" font-family="Arimo,Arial,sans-serif" font-size="11" fill="#3f8ccc">60%</text>
  </svg>
  <div class="mo-right">
    <div class="mo-item" style="margin-bottom:8px"><p class="mo-head">Heading Text</p><p class="mo-text" style="font-weight:400">dolore aliqua. Lorem ipsum dolor sit amet, consectetur adipiscing elit, sed do eiusmod tempor incididunt ut</p></div>
    <div class="mo-item"><p class="mo-head">Heading Text</p><p class="mo-text" style="font-weight:400">dolore aliqua. Lorem ipsum dolor sit amet, consectetur adipiscing elit, sed do eiusmod tempor incididunt ut</p></div>
  </div>
  <div class="mo-card">
    <h3>Heading Text</h3>
    <p>dolore aliqua. Lorem ipsum dolor sit amet, consectetur adipiscing elit, sed do eiusmod tempor incididunt ut labore Lorem ipsum dolor sit amet, consectetur adipiscing elit, sed do eiusmod tempor incididunt ut labore et dolore aliqua. Lorem ipsum dolor sit amet, consectetur adipiscing elit, sed do eiusmod tempor incididunt ut labore dolore aliqua. Lorem ipsum dolor sit amet, consectetur adipiscing elit, sed do eiusmod tempor incididunt ut labore Lorem ipsum dolor sit amet, consectetur adipiscing elit, sed do eiusmod tempor incididunt ut labore et dolore aliqua.</p>
  </div>
  <p class="footer">© Keelway Company · www.keelwayco.com/000-000-0000</p>
</section>

<!-- Mock up -->
<section class="slide col-r row4">
  <h2 class="slide-title">Mock Up</h2>
  <div class="side-band"><div class="brand brand-sm"><span class="dot"></span>KEELWAY</div><span class="page-no">8</span></div>
  <div class="photo" role="img" aria-label="Desktop monitor and laptop showing light bulb and ocean photos" style="left:8px;top:34px;width:188px;height:150px;background:radial-gradient(ellipse at 45% 45%,#8a9aa8 0%,#c9d0d6 45%,#ffffff 75%)"></div>
  <ul class="mini-list body-copy" style="position:absolute;left:200px;top:70px;width:92px">
    <li>Lorem ipsum dolor sit amet, consectetur adipiscing elit, sed do eiusmod tempor incididunt ut labore.</li>
    <li>Ut enim ad minim veniam, quis nostrud exercitation ullamco laboris nisi ut aliquip ex ea commodo consequat duis aute.</li>
  </ul>
  <p class="footer">© Keelway Company · www.keelwayco.com/000-000-0000</p>
</section>

<!-- Infographic -->
<section class="slide col-l row5">
  <h2 class="slide-title">Infographic</h2>
  <div class="side-band"><div class="brand brand-sm"><span class="dot"></span>KEELWAY</div><span class="page-no">9</span></div>
  <ul class="mini-list body-copy" style="position:absolute;left:10px;top:60px;width:78px">
    <li>Lorem ipsum dolor sit amet, consectetur adipiscing elit, sed do eiusmod tempor incididunt ut labore.</li>
    <li>Ut enim ad minim veniam, quis nostrud exercitation ullamco laboris nisi ut aliquip ex ea commodo consequat duis aute.</li>
  </ul>
  <div class="photo" role="img" aria-label="Four-step infographic graphic in teal, orange, grey and lilac" style="left:100px;top:42px;width:172px;height:140px;border-radius:4px;background:linear-gradient(90deg,#9fcdc3 0%,#e98a68 35%,#d6dadd 65%,#c3b7dc 100%)"></div>
  <p class="footer">© Keelway Company · www.keelwayco.com/000-000-0000</p>
</section>

<!-- Our team, single -->
<section class="slide col-r row5">
  <p style="position:absolute;left:14px;top:16px;font-size:8px;color:#333">• OUR TEAM</p>
  <div class="side-band"><div class="brand brand-sm"><span class="dot"></span>KEELWAY</div><span class="page-no">10</span></div>
  <div class="avatar" role="img" aria-label="Portrait photo of the CEO" style="position:absolute;left:125px;top:33px;width:54px;height:54px"></div>
  <div style="position:absolute;left:88px;top:92px;width:128px;text-align:center">
    <p style="font-size:4.6px;font-weight:700;color:#333">Mr. John Smith</p>
    <p style="font-size:4.6px;font-weight:700;color:#333;margin-bottom:2px">CEO</p>
    <p class="body-copy" style="text-align:center;font-size:3.7px">Lorem ipsum dolor sit amet, consectetur adipiscing elit, sed do eiusmod tempor incididunt ut labore et dolore magna aliqua. Duis aute irure dolor in reprehenderit in voluptate velit esse cillum dolore eu fugiat nulla pariatur.</p>
    <div style="display:flex;justify-content:center;gap:2.5px;margin-top:3px">
      <span style="width:5px;height:5px;border-radius:50%;background:var(--blue)"></span>
      <span style="width:5px;height:5px;border-radius:50%;background:var(--blue)"></span>
      <span style="width:5px;height:5px;border-radius:50%;background:var(--blue)"></span>
      <span style="width:5px;height:5px;border-radius:50%;background:var(--blue)"></span>
    </div>
  </div>
  <p class="footer">© Keelway Company · www.keelwayco.com/000-000-0000</p>
</section>

<!-- Our team, four -->
<section class="slide col-l row6">
  <h2 class="slide-title">Our Team</h2>
  <div class="side-band"><div class="brand brand-sm"><span class="dot"></span>KEELWAY</div><span class="page-no">11</span></div>
  <div class="team-entry" style="left:14px;top:40px">
    <div class="avatar" role="img" aria-label="Portrait photo of Michael Doe"></div>
    <div><p class="team-name">Michael Doe</p><p class="team-role">CEO</p><p class="team-deg">MS(MPT), MBA and CMA Dip. PM</p>
    <ul class="mini-list body-copy"><li>Lorem ipsum dolor sit amet, consectetur adipiscing elit</li><li>sed do eiusmod tempor incididunt ut labore et dolore magna aliqua.</li><li>Ut enim ad minim veniam, quis nostrud exercitation</li></ul></div>
  </div>
  <div class="team-entry" style="left:170px;top:40px">
    <div class="avatar" role="img" aria-label="Portrait photo of James Doe"></div>
    <div><p class="team-name">James Doe</p><p class="team-role">Manager</p><p class="team-deg">M.B.A</p>
    <ul class="mini-list body-copy"><li>Lorem ipsum dolor sit amet, consectetur adipiscing elit</li><li>sed do eiusmod tempor incididunt ut labore et dolore magna aliqua.</li><li>Ut enim ad minim veniam, quis nostrud exercitation</li></ul></div>
  </div>
  <div class="team-entry" style="left:14px;top:110px">
    <div class="avatar" role="img" aria-label="Portrait photo of Jane Doe"></div>
    <div><p class="team-name">Jane Doe</p><p class="team-role">Doctor of Chemistry</p><p class="team-deg">M.B.A</p>
    <ul class="mini-list body-copy"><li>Lorem ipsum dolor sit amet, consectetur adipiscing elit</li><li>sed do eiusmod tempor incididunt ut labore et dolore magna aliqua.</li><li>Ut enim ad minim veniam, quis nostrud exercitation</li></ul></div>
  </div>
  <div class="team-entry" style="left:170px;top:110px">
    <div class="avatar" role="img" aria-label="Portrait photo of John Doe"></div>
    <div><p class="team-name">John Doe</p><p class="team-role">Doctor of Physical</p><p class="team-deg">Professor</p>
    <ul class="mini-list body-copy"><li>Lorem ipsum dolor sit amet, consectetur adipiscing elit</li><li>sed do eiusmod tempor incididunt ut labore et dolore magna aliqua.</li><li>Ut enim ad minim veniam, quis nostrud exercitation</li></ul></div>
  </div>
  <p class="footer">© Keelway Company · www.keelwayco.com/000-000-0000</p>
</section>

<!-- Thank you -->
<section class="slide col-r row6" style="background:var(--blue)">
  <div class="photo" role="img" aria-label="Row of hanging light bulbs, blue tinted" style="inset:0;background:linear-gradient(135deg,#1e537e 0%,#2f6793 50%,#20557f 100%)"></div>
  <div class="cover-ring" style="left:-40px;top:-20px;width:210px;height:210px;border-color:rgba(190,196,200,.55)"></div>
  <div class="brand brand-lg" style="left:172px;top:52px"><span class="dot"></span>KEELWAY</div>
  <p class="thanks">Thank you...</p>
  <ul class="contact">
    <li><svg viewBox="0 0 10 10"><path d="M5 .5a3.3 3.3 0 0 0-3.3 3.3C1.7 6.5 5 9.5 5 9.5s3.3-3 3.3-5.7A3.3 3.3 0 0 0 5 .5z" fill="#fff"/><circle cx="5" cy="3.8" r="1.2" fill="#245d8c"/></svg><span>123 Street Road<br>City 12345</span></li>
    <li><svg viewBox="0 0 10 10"><path d="M2 1h2l1 2.5-1.3.8a5.5 5.5 0 0 0 2 2l.8-1.3L9 6v2a1 1 0 0 1-1 1A7 7 0 0 1 1 2a1 1 0 0 1 1-1z" fill="#fff"/></svg><span>(123) 456-7890</span></li>
    <li><svg viewBox="0 0 10 10"><rect x=".5" y="2" width="9" height="6" rx=".8" fill="#fff"/><path d="M.8 2.4 5 5.6l4.2-3.2" fill="none" stroke="#245d8c" stroke-width=".8"/></svg><span>emailaddress@email.com</span></li>
    <li><svg viewBox="0 0 10 10"><circle cx="5" cy="5" r="4.3" fill="none" stroke="#fff" stroke-width="1"/><path d="M.8 5h8.4M5 .7c-2.4 2.6-2.4 6 0 8.6M5 .7c2.4 2.6 2.4 6 0 8.6" fill="none" stroke="#fff" stroke-width=".7"/></svg><span>www.website-address.com</span></li>
  </ul>
</section>

</body>
</html>
```